Signs to Go on the Side of Shipping Containers

We are a startup in North Alabama that will lease/sale shipping containers as Portable Storage options for business/construction sites. We need signs that will be mass produced and be mounted on every side of the container for advertising/visibility.
We need multiple sizes depending on the side the sign will be on/ the size of the container it is being mounted on.
Website: www.ridgelinebinworks.com

MUST BE SIMPLE AND EASY TO READ. Not to Busy. See example in
Updates

One designer is asking me to extend deadline. This is my first design project so not sure why they want me to do this but figured I would.

Target Market(s)

Business owners/Construction Companies/Individuals Moving

Industry/Entity Type

Portable Storage

Colors
0054AA
0677BA
7BADD7
CADEEF
E8F1F8

Requirements
Must have
• Company Name(Ridgeline Bin Works)/Phone Number (256-555-0147)/Website (www.ridgelinebinworks.com
Nice to have
• Play on the container shapes/pattern.

```html
<!DOCTYPE html>
<html lang="en">
<head>
<meta charset="utf-8">
<title>Ridgeline Bin Works – Container Sign</title>
<link rel="stylesheet" href="https://fonts.googleapis.com/css2?family=Rubik:wght@900&family=Montserrat:wght@500;700&display=swap">
<style>
  :root {
    --blue-deep: #0054AA;
    --blue-mid: #0677BA;
    --blue-soft: #7BADD7;
    --blue-pale: #CADEEF;
    --blue-mist: #E8F1F8;
    --navy: #1C2F5C;
    --band: #1F3E73;
    --white: #FFFFFF;
    --page: #FFFFFF;
  }
  * { margin: 0; padding: 0; box-sizing: border-box; }
  html, body {
    width: 1163px;
    height: 1200px;
    overflow: hidden;
    background: var(--page);
  }
  .canvas {
    width: 1163px;
    height: 1200px;
    display: flex;
    align-items: center;
    justify-content: center;
  }
  .sign {
    position: relative;
    width: 1063px;
    height: 370px;
    overflow: hidden;
    background: linear-gradient(180deg, var(--blue-mid) 0%, #3D8FCB 40%, var(--blue-soft) 72%, var(--blue-pale) 100%);
    display: flex;
    flex-direction: column;
    align-items: center;
  }
  .sign__map {
    position: absolute;
    left: 60px;
    top: 12px;
    width: 940px;
    height: 300px;
    border-radius: 50%;
    background: radial-gradient(ellipse at center, rgba(232,241,248,0.38) 0%, rgba(202,222,239,0.18) 55%, rgba(202,222,239,0) 75%);
  }
  .sign__name {
    position: relative;
    margin-top: 40px;
    font-family: "Rubik", sans-serif;
    font-weight: 900;
    color: var(--white);
    text-align: center;
    text-transform: uppercase;
    line-height: 0.9;
  }
  .sign__name-top {
    display: block;
    font-size: 74px;
    letter-spacing: 1px;
  }
  .sign__name-main {
    display: block;
    font-size: 128px;
    letter-spacing: -1px;
  }
  .sign__tagline {
    position: relative;
    margin-top: 18px;
    padding: 6px 28px;
    background: var(--band);
    color: var(--blue-mist);
    font-family: "Montserrat", sans-serif;
    font-weight: 500;
    font-size: 18px;
    letter-spacing: 1.6px;
    text-transform: uppercase;
    border-left: 6px solid var(--blue-deep);
    border-right: 6px solid var(--blue-deep);
  }
  .sign__contacts {
    position: relative;
    width: 870px;
    margin-top: 24px;
    display: flex;
    justify-content: space-between;
    align-items: center;
    font-family: "Montserrat", sans-serif;
    font-weight: 700;
    font-size: 29px;
    color: var(--navy);
  }
  .contact {
    display: flex;
    align-items: center;
    gap: 12px;
  }
  .contact__icon {
    width: 26px;
    height: 26px;
    fill: var(--navy);
  }
</style>
</head>
<body>
  <main class="canvas">
    <section class="sign">
      <div class="sign__map" role="img" aria-label="Faint world map in light blue behind the company name"></div>

      <h1 class="sign__name">
        <span class="sign__name-top">Ridgeline</span>
        <span class="sign__name-main">Bin Works</span>
      </h1>

      <p class="sign__tagline">Buy or rent shipping containers</p>

      <div class="sign__contacts">
        <span class="contact contact--web">
          <svg class="contact__icon" viewBox="0 0 24 24" aria-hidden="true">
            <circle cx="12" cy="12" r="11"/>
            <path d="M12 1.5v21M1.5 12h21M4 6.5h16M4 17.5h16M12 1.5c-4 3-4 18 0 21M12 1.5c4 3 4 18 0 21" stroke="#CADEEF" stroke-width="1.4" fill="none"/>
          </svg>
          ridgelinebinworks.com
        </span>
        <span class="contact contact--phone">
          <svg class="contact__icon" viewBox="0 0 24 24" aria-hidden="true">
            <path d="M6.6 10.8c1.4 2.8 3.8 5.1 6.6 6.6l2.2-2.2c.3-.3.7-.4 1-.2 1.1.4 2.3.6 3.6.6.6 0 1 .4 1 1V20c0 .6-.4 1-1 1C10.6 21 3 13.4 3 4c0-.6.4-1 1-1h3.5c.6 0 1 .4 1 1 0 1.3.2 2.5.6 3.6.1.3 0 .7-.2 1L6.6 10.8z"/>
          </svg>
          256-555-0147
        </span>
      </div>
    </section>
  </main>
</body>
</html>
```